Velmora Water Purification

We need a website set up on a "Free account" WordPress platform. (This is the type of Wordpress site that you can sign up for and create online for free (not a server-hosted type.)
The website will be for a water purification company. They install devices in homes to purify the water for safer drinking, bathing, and cleaning.
Our logo is attached. Please keep color scheme of the website consistent with the logo.
Water Purification

```html
<!DOCTYPE html>
<html lang="en">
<head>
<meta charset="utf-8">
<title>Velmora Water Purification</title>
<link href="https://fonts.googleapis.com/css2?family=Raleway:wght@500;600;700;800&family=Open+Sans:ital,wght@0,400;0,600;1,400&display=swap" rel="stylesheet">
<style>
:root{
  --navy:#24297a;
  --navy-deep:#1c2266;
  --sky:#19a3df;
  --sky-light:#3cb8ee;
  --ink:#333;
  --muted:#555;
  --line:#d9d9d9;
  --panel:#f3f3f3;
  --white:#fff;
}
*{margin:0;padding:0;box-sizing:border-box}
html,body{width:1200px;height:2605px;overflow:hidden;background:var(--white)}
body{font-family:"Open Sans",sans-serif;color:var(--ink);position:relative}
.head,.title{font-family:"Raleway",sans-serif}
section,header,footer{position:relative;width:1200px}

/* header */
.site-header{height:99px;background:#f6f6f6;z-index:3}
.brand{position:absolute;left:152px;top:0;width:252px;height:146px;background:var(--white);border-radius:0 0 126px 126px/0 0 60px 60px;display:flex;align-items:center;justify-content:center;text-align:center}
.brand-name{font-family:"Raleway",sans-serif;font-weight:700;font-size:21px;line-height:1.2;color:var(--navy);width:190px;margin-top:14px}
.phone{position:absolute;right:160px;top:18px;font-family:"Raleway",sans-serif;font-size:16px;color:var(--sky);display:flex;align-items:center;gap:8px;letter-spacing:.3px}
.main-nav{position:absolute;right:162px;top:64px;display:flex;gap:26px;font-family:"Raleway",sans-serif;font-weight:600;font-size:11.5px;color:#222}
.main-nav a{display:flex;align-items:center;gap:5px;text-decoration:none;color:inherit}
.main-nav a::before{content:"";width:6px;height:8px;border-radius:50% 50% 50% 50%/60% 60% 40% 40%;background:#c7c7c7}
.main-nav a.active{color:var(--sky)}
.main-nav a.active::before{background:var(--sky)}

/* hero */
.hero{height:509px;overflow:hidden}
.hero-photo{position:absolute;inset:0;background:linear-gradient(100deg,#1f6fd0 0%,#4a9be4 35%,#cfe3f3 62%,#eef3f7 80%,#b9d3ea 100%)}
.hero-title{position:absolute;left:159px;top:112px;font-weight:800;font-size:46px;line-height:53px;color:var(--white);letter-spacing:.5px}
.slider-dots{position:absolute;left:577px;top:552px;display:flex;gap:6px}
.hero .slider-dots{top:453px}
.slider-dots span{width:11px;height:11px;border-radius:50%;background:rgba(255,255,255,.55)}
.slider-dots span.on{background:var(--white)}

/* purpose band */
.purpose{height:318px;background:linear-gradient(90deg,var(--navy-deep) 0%,#2b4fa7 45%,var(--sky) 100%);color:var(--white)}
.purpose h2{position:absolute;left:160px;top:83px;font-weight:700;font-size:29px;line-height:35px}
.purpose p{position:absolute;left:160px;top:176px;width:360px;font-size:10.5px;line-height:21px;opacity:.95}
.uses{position:absolute;left:620px;top:70px;display:flex;gap:14px}
.use{width:128px;text-align:center}
.use-ring{width:128px;height:128px;border-radius:50%;border:7px solid var(--navy);background:var(--white);box-shadow:0 0 0 5px rgba(255,255,255,.9);display:flex;align-items:center;justify-content:center}
.use-ring .inner{width:92px;height:92px;border-radius:50%;background:var(--navy);display:flex;align-items:center;justify-content:center}
.use span{display:block;margin-top:18px;font-family:"Raleway",sans-serif;font-weight:600;font-size:18px}

/* about */
.about{height:438px}
.about-photo{position:absolute;left:161px;top:61px;width:461px;height:312px;background:linear-gradient(135deg,#e8d9b6 0%,#d9c79c 40%,#5c7fb8 70%,#2f4f8f 100%)}
.play{position:absolute;left:190px;top:116px;width:80px;height:80px;border-radius:50%;background:rgba(255,255,255,.85);border:5px solid var(--navy);display:flex;align-items:center;justify-content:center}
.about h2{position:absolute;left:658px;top:66px;width:380px;font-weight:700;font-size:30px;line-height:36px;color:var(--navy)}
.about p{position:absolute;left:658px;top:144px;width:382px;font-size:10.5px;line-height:21.6px;color:var(--muted);text-align:justify}
.btn{display:inline-block;background:var(--sky);color:var(--white);font-family:"Raleway",sans-serif;font-size:12px;border-radius:18px;text-align:center}
.about .btn{position:absolute;left:658px;top:333px;width:104px;height:35px;line-height:35px}

/* works */
.works{height:460px;background:var(--panel);border-top:1px solid #e6e6e6;border-bottom:1px solid #e6e6e6}
.works h2{position:absolute;top:48px;width:100%;text-align:center;font-weight:700;font-size:30px;color:var(--navy)}
.cards{position:absolute;left:161px;top:109px;display:flex;gap:25px}
.card{width:201px;height:300px;background:var(--white)}
.card-photo{height:132px}
.card h3{margin-top:22px;text-align:center;font-family:"Raleway",sans-serif;font-weight:700;font-size:13px;color:var(--sky)}
.card p{margin:16px auto 0;width:165px;text-align:center;font-size:11px;line-height:21px;color:var(--muted)}

/* info row */
.info{height:474px}
.col{position:absolute;top:68px}
.col h2{font-weight:700;font-size:23px;color:var(--navy)}
.col h2::after{content:"";display:block;width:245px;height:4px;margin-top:12px;background:linear-gradient(90deg,var(--sky) 0 50px,#e3e3e3 50px)}
.contact-col{left:160px}
.field{width:240px;height:33px;margin-top:5px;border:1px solid var(--line);font-size:10px;padding:8px 10px;color:#444}
.field.first{margin-top:40px}
.field.msg{height:105px}
.contact-col .btn{margin-top:16px;width:103px;height:35px;line-height:35px}
.news-col{left:479px}
.news-item{margin-top:38px;width:245px}
.news-item+.news-item{margin-top:26px}
.news-date{font-size:10px;font-weight:600;color:var(--navy);display:flex;align-items:center;gap:6px}
.news-item p{margin-top:12px;font-size:10.5px;line-height:20.5px;color:#444}
.news-col .btn{margin-top:28px;width:104px;height:35px;line-height:35px}
.quote-col{left:794px}
.quote-col blockquote{margin-top:38px;width:250px;font-style:italic;font-size:10.5px;line-height:20px;color:#444}
.quote-col blockquote b{color:var(--navy);font-style:normal}
.author{margin-top:22px;display:flex;align-items:center;gap:30px}
.author-photo{width:100px;height:100px;border-radius:50%;border:4px solid #e5e5e5;background:linear-gradient(160deg,#c9cfd6,#6f7883)}
.author strong{display:block;font-family:"Raleway",sans-serif;font-weight:600;font-size:12px;color:var(--sky)}
.author span{display:block;margin-top:4px;font-size:12px;font-weight:600;color:#222}

/* footer */
.site-footer{height:247px;background:var(--navy);color:var(--white)}
.f-col{position:absolute;top:46px}
.f-col h4{font-family:"Raleway",sans-serif;font-weight:700;font-size:15px;margin-bottom:22px}
.f-col li{list-style:none;font-size:10.5px;line-height:21px;opacity:.92}
.f-contact{left:161px;width:170px}
.f-contact li{display:flex;gap:8px;align-items:flex-start}
.f-contact li svg{flex:none;margin-top:5px}
.sub-footer{height:60px;background:var(--navy-deep);color:var(--white)}
.socials{position:absolute;left:161px;top:19px;display:flex;gap:11px}
.socials span{width:24px;height:24px;border-radius:50%;border:1.5px solid var(--white)}
.copyright{position:absolute;right:161px;top:22px;font-size:10.5px}
</style>
</head>
<body>

<header class="site-header">
  <div class="brand"><div class="brand-name">Velmora Water Purification</div></div>
  <div class="phone">
    <svg width="20" height="20" viewBox="0 0 24 24" fill="none" stroke="currentColor" stroke-width="1.6"><path d="M5 3h4l2 5-2.5 1.5a11 11 0 0 0 6 6L16 13l5 2v4a2 2 0 0 1-2 2A16 16 0 0 1 3 5a2 2 0 0 1 2-2z"/></svg>
    PHONE: 0800 412 73 90
  </div>
  <nav class="main-nav">
    <a class="active">HOME</a><a>ABOUT</a><a>SERVICES</a><a>PRODUCTS</a><a>INSTALL</a><a>BLOG</a><a>CONTACT</a>
  </nav>
</header>

<section class="hero">
  <div class="hero-photo" role="img" aria-label="Photo of a reverse osmosis filtration unit with blue filter housings and a chrome faucet"></div>
  <h1 class="hero-title head">WATER<br>PURIFICATION<br>SYSTEMS</h1>
  <div class="slider-dots"><span></span><span></span><span class="on"></span></div>
</section>

<section class="purpose">
  <h2 class="head">Install devices in homes<br>to purify the water</h2>
  <p>Sed ut perspiciatis unde omnis iste natus error sit voluptatem accus antium doloremque laudantium, totam rem aperiam, eaque ipsa quae ab illo inventore veritatis quasi architecto beatae.</p>
  <div class="uses">
    <div class="use">
      <div class="use-ring"><div class="inner">
        <svg width="50" height="50" viewBox="0 0 50 50" fill="none" stroke="#fff" stroke-width="2.4"><rect x="18" y="6" width="12" height="6" rx="1"/><path d="M17 12h14l3 7v23a3 3 0 0 1-3 3H17a3 3 0 0 1-3-3V19z"/><path d="M14 24h20"/><path d="M30 30c0 0-4 5-4 8a4 4 0 0 0 8 0c0-3-4-8-4-8z" fill="#fff"/></svg>
      </div></div>
      <span>Safer Drinking</span>
    </div>
    <div class="use">
      <div class="use-ring"><div class="inner">
        <svg width="54" height="50" viewBox="0 0 54 50" fill="none" stroke="#fff" stroke-width="2.4"><path d="M8 26V10a5 5 0 0 1 10 0"/><path d="M4 26h46v6a10 10 0 0 1-10 10H14A10 10 0 0 1 4 32z"/><path d="M14 42l-3 5M40 42l3 5"/><circle cx="26" cy="19" r="3"/><circle cx="34" cy="16" r="4"/><circle cx="42" cy="20" r="3"/></svg>
      </div></div>
      <span>Bathing</span>
    </div>
    <div class="use">
      <div class="use-ring"><div class="inner">
        <svg width="50" height="50" viewBox="0 0 50 50" fill="none" stroke="#fff" stroke-width="2.4"><path d="M38 4L30 34"/><path d="M24 34h14l4 10H20z"/><path d="M8 22h16l-2 22H10z"/><path d="M6 22h20"/><path d="M12 16h8v6h-8z"/></svg>
      </div></div>
      <span>Cleaning</span>
    </div>
  </div>
</section>

<section class="about">
  <div class="about-photo" role="img" aria-label="Video still of a technician installing a filtration tank under a kitchen sink"></div>
  <div class="play" style="left:351px;top:177px">
    <svg width="26" height="28" viewBox="0 0 26 28"><path d="M5 2l19 12L5 26z" fill="#24297a"/></svg>
  </div>
  <h2 class="head">Install water purification systems in homes</h2>
  <p>Sed ut perspiciatis unde omnis iste natus error sit voluptatem accusantium doloremque laudantium, totam rem aperiam, eaque ipsa quae ab illo inventore veritatis quasi architecto beatae vitae dicta sunt explicabo. Nemo enim ipsam voluptatemui voluptas sit aspernatur aut odit aut fugit, sed quia consequuntur magni dolores eos qui ratione voluptatem sequi nesciunt. Neque porro quisquam est, qui dolorem ipsum quia dolor sit amet, consectetur, adipisci velit, sed quia non numquam eius modi tempora incidunt ut labore et dolore magnam aliquam ratione voluptatem sequi.</p>
  <a class="btn">Read More</a>
</section>

<section class="works">
  <h2 class="head">Installation Works</h2>
  <div class="cards">
    <article class="card">
      <div class="card-photo" role="img" aria-label="Photo of a filter unit being fitted in a kitchen cabinet" style="background:linear-gradient(135deg,#8a6a4c,#d8d4cc 60%,#3d5d9c)"></div>
      <h3>Finibus Bonorum</h3>
      <p>Sed ut perslorepiciatis une omnis iste natus sit voluptam accusantiumuerslorepiciatis une omnis iste nat.</p>
    </article>
    <article class="card">
      <div class="card-photo" role="img" aria-label="Photo of a row of blue filter housings" style="background:linear-gradient(90deg,#1d4fb0,#3a7fd8 45%,#c9d8e8 75%,#8fa9c7)"></div>
      <h3>Finibus Bonorum</h3>
      <p>Sed ut perslorepiciatis une omnis iste natus sit voluptam accusantiumuerslorepiciatis une omnis iste nat.</p>
    </article>
    <article class="card">
      <div class="card-photo" role="img" aria-label="Photo of a countertop purifier with faucet" style="background:linear-gradient(160deg,#2a6fd6,#5ea2e6 50%,#e6eef6)"></div>
      <h3>Finibus Bonorum</h3>
      <p>Sed ut perslorepiciatis une omnis iste natus sit voluptam accusantiumuerslorepiciatis une omnis iste nat.</p>
    </article>
    <article class="card">
      <div class="card-photo" role="img" aria-label="Photo of a glass being filled with purified water" style="background:linear-gradient(135deg,#e9e4de,#f4f1ee 50%,#c8b7a6)"></div>
      <h3>Finibus Bonorum</h3>
      <p>Sed ut perslorepiciatis une omnis iste natus sit voluptam accusantiumuerslorepiciatis une omnis iste nat.</p>
    </article>
  </div>
</section>

<section class="info">
  <div class="col contact-col">
    <h2 class="head">Contact Form</h2>
    <div class="field first">Name:</div>
    <div class="field">Email:</div>
    <div class="field">Phone:</div>
    <div class="field msg">Message:</div>
    <a class="btn">Submit</a>
  </div>
  <div class="col news-col">
    <h2 class="head">Latest News</h2>
    <div class="news-item">
      <div class="news-date"><svg width="10" height="10" viewBox="0 0 10 10" fill="none" stroke="#24297a" stroke-width="1.2"><rect x="1" y="2" width="8" height="7"/><path d="M1 4.5h8M3 1v2M7 1v2"/></svg>Nov 14,2017</div>
      <p>Ut enim alord minim veniam, quis nostrud exeron ullamco laboris nisi ut aliquip exlor ea commodns equatis aute irure dolor derit in voluptat.</p>
    </div>
    <div class="news-item">
      <div class="news-date"><svg width="10" height="10" viewBox="0 0 10 10" fill="none" stroke="#24297a" stroke-width="1.2"><rect x="1" y="2" width="8" height="7"/><path d="M1 4.5h8M3 1v2M7 1v2"/></svg>Nov 14,2017</div>
      <p>Ut enim alord minim veniam, quis nostrud exeron ullamco laboris nisi ut aliquip exlor ea commodns equatis aute irure dolor derit in voluptat.</p>
    </div>
    <a class="btn">Read More</a>
  </div>
  <div class="col quote-col">
    <h2 class="head">Testimonials</h2>
    <blockquote><b>“</b> Ut enim alord minim veniam, quis nostrud exelo ullamco laboris nisi ut aliquip exlloror ea commons equatis aute irure doloelor derit in voluptatUt enim al ord minim venialorem, quis nostrud exeron ullamcol abo ris nisi ut aliquip exlor ea commodnsequa tis aut irure dolor derit in voluptat. <b>”</b></blockquote>
    <div class="author">
      <div class="author-photo" role="img" aria-label="Portrait of the client giving the testimonial"></div>
      <div><strong>Dara Ellison,</strong><span>City Name</span></div>
    </div>
  </div>
</section>

<footer class="site-footer">
  <div class="f-col f-contact">
    <h4>CONTACT US</h4>
    <ul>
      <li><svg width="8" height="11" viewBox="0 0 8 11"><path d="M4 0a4 4 0 0 1 4 4c0 3-4 7-4 7S0 7 0 4a4 4 0 0 1 4-4z" fill="#fff"/><circle cx="4" cy="4" r="1.4" fill="#24297a"/></svg>Our Location Dummy loremu 897, loremusm dolor dummy 847 location</li>
      <li><svg width="9" height="9" viewBox="0 0 24 24"><path d="M5 3h4l2 5-2.5 1.5a11 11 0 0 0 6 6L16 13l5 2v4a2 2 0 0 1-2 2A16 16 0 0 1 3 5a2 2 0 0 1 2-2z" fill="#fff"/></svg>Phone: 555 318 2047</li>
      <li><svg width="10" height="8" viewBox="0 0 10 8"><rect width="10" height="8" fill="#fff"/><path d="M0 0l5 4 5-4" stroke="#24297a" fill="none"/></svg>Email: hello@velmorawater.example</li>
    </ul>
  </div>
  <div class="f-col" style="left:380px">
    <h4>SERVICES</h4>
    <ul><li>Containerised Systems</li><li>Processes</li><li>Design</li><li>Install</li><li>Commission</li><li>Refurbish</li></ul>
  </div>
  <div class="f-col" style="left:568px">
    <h4>LINKS</h4>
    <ul><li>Sed ut perspiciatis undemn</li><li>Rste natus error sit volu</li><li>Htatem accusantium dol</li><li>Oremque laud</li><li>Rste natus error sit volu</li><li>Htatem accusa</li></ul>
  </div>
  <div class="f-col" style="left:778px">
    <h4>ABOUT</h4>
    <ul><li>Deionisation</li><li>Reverse Osmosis</li><li>Water Filtration</li><li>Water Recycling</li><li>Ultra Filtration</li><li>Purification systems</li></ul>
  </div>
  <div class="f-col" style="left:946px">
    <h4>OTHER</h4>
    <ul><li>About Us</li><li>Contact Us</li><li>Forum</li><li>Support team</li><li>Careers</li><li>Blog</li></ul>
  </div>
</footer>

<div class="sub-footer" style="position:relative;width:1200px">
  <div class="socials"><span></span><span></span><span></span><span></span><span></span></div>
  <div class="copyright">© 2017 All Copyrights Reserved. Privacy Policy Terms and Conditions</div>
</div>

</body>
</html>
```